Hal's Remedies Business Card Design Project

I need a business card designed for my pharmacy Hal's Remedies. I would like just the logo on one side, maybe with black background and white lettering. The other side I would also like to include my logo which is attached. Also, please include my name and the following information:
Hal Norwick Owner/Pharm D.
Business address is 7163 N Birch Rd Sioux Falls, SD 57291.
Phone number is 605-318-6027 and fax # is 605-318-6031.
my email address is hal@halsremedies.example.
My website is www.halsremedies.example.
My business hours are Monday-Friday 8am-7 pm. Saturday 8am-12 pm. Sunday Closed.
I would like the design to include my logo colors, black, white, and neon green. Silver may be added as a highlight. Thanks.
Pharmacy
See above in product description

```html
<!DOCTYPE html>
<html lang="en">
<head>
<meta charset="utf-8">
<title>Hal's Remedies – Business Card</title>
<link rel="stylesheet" href="https://fonts.googleapis.com/css2?family=Open+Sans:wght@600&family=Arimo:wght@400;700&family=Lora:ital,wght@1,700&display=swap">
<style>
  :root {
    --ink: #1a1818;
    --lime: #9ac43c;
    --white: #ffffff;
    --stage: #ececec;
  }
  * { margin: 0; padding: 0; box-sizing: border-box; }
  html, body { width: 974px; height: 1200px; overflow: hidden; }
  body { background: var(--stage); position: relative; font-family: "Arimo", Arial, sans-serif; }

  .card { position: absolute; left: 77px; width: 801px; height: 468px; overflow: hidden; }
  .card--front { top: 93px; background: var(--ink); }
  .card--back { top: 635px; background: var(--ink); }

  .brand-dot { position: absolute; border-radius: 50%; background: var(--lime); }
  .card--front .brand-dot { left: 78px; top: 177px; width: 80px; height: 80px; }

  .brand-name { position: absolute; font-family: "Open Sans", Arial, sans-serif; font-weight: 600; color: var(--white); white-space: nowrap; letter-spacing: -0.5px; }
  .card--front .brand-name { left: 190px; top: 168px; font-size: 60px; }

  .website { position: absolute; font-family: "Lora", Georgia, serif; font-style: italic; font-weight: 700; color: var(--lime); white-space: nowrap; }
  .card--front .website { right: 39px; top: 260px; font-size: 22px; }

  .back-panel { position: absolute; left: 0; top: 0; width: 373px; height: 468px; background: var(--lime); }
  .back-panel .brand-name { left: 0; right: 0; top: 212px; text-align: center; font-size: 29px; }

  .details-rule { position: absolute; left: 396px; top: 55px; width: 2px; height: 237px; background: var(--lime); }
  .holder-name { position: absolute; left: 415px; top: 54px; font-size: 29px; color: var(--lime); }
  .holder-title { position: absolute; left: 415px; top: 88px; font-size: 21px; color: var(--white); }
  .title-rule { position: absolute; left: 415px; top: 120px; width: 345px; height: 2px; background: var(--lime); }

  .contact { position: absolute; left: 450px; color: var(--white); font-size: 23px; line-height: 1; white-space: nowrap; }
  .contact strong { font-weight: 700; }
  .contact--light { font-weight: 400; }
  .icon { position: absolute; left: 412px; fill: var(--lime); }

  .hours { position: absolute; left: 450px; top: 310px; font-size: 20px; line-height: 25px; color: var(--white); }
  .hours b { color: var(--lime); font-weight: 700; }

  .card--back .website { left: 433px; top: 412px; font-size: 23px; }
</style>
</head>
<body>

<section class="card card--front" aria-label="Card front">
  <span class="brand-dot"></span>
  <div class="brand-name">Hal's Remedies</div>
  <div class="website">www.halsremedies.example</div>
</section>

<section class="card card--back" aria-label="Card back">
  <div class="back-panel">
    <div class="brand-name">Hal's Remedies</div>
  </div>

  <span class="details-rule"></span>
  <div class="holder-name">Hal Norwick</div>
  <div class="holder-title">Owner/Pharm D.</div>
  <span class="title-rule"></span>

  <svg class="icon" style="top:137px" width="30" height="50" viewBox="0 0 30 50" aria-hidden="true">
    <path d="M15 0C6.7 0 0 6.7 0 15c0 11 15 35 15 35s15-24 15-35C30 6.7 23.3 0 15 0zm0 21a6 6 0 1 1 0-12 6 6 0 0 1 0 12z"/>
  </svg>
  <div class="contact" style="top:141px"><strong>7163 N Birch Rd Sioux Falls,</strong></div>
  <div class="contact contact--light" style="top:172px">SD 57291.</div>

  <svg class="icon" style="top:205px" width="32" height="26" viewBox="0 0 32 26" aria-hidden="true">
    <path d="M2 8c0-4 6-6 14-6s14 2 14 6v3h-7V8H9v3H2z"/>
    <path d="M6 12h20l3 12H3z"/>
    <circle cx="16" cy="18" r="3" fill="#1a1818"/>
  </svg>
  <div class="contact" style="top:206px"><strong>605-318-6027</strong></div>

  <svg class="icon" style="top:236px" width="30" height="28" viewBox="0 0 30 28" aria-hidden="true">
    <rect x="7" y="0" width="16" height="8"/>
    <rect x="0" y="9" width="30" height="12" rx="2"/>
    <rect x="7" y="18" width="16" height="10" fill="#1a1818" stroke="#9ac43c" stroke-width="2"/>
  </svg>
  <div class="contact" style="top:238px"><strong>605-318-6031.</strong></div>

  <svg class="icon" style="top:275px" width="28" height="20" viewBox="0 0 28 20" aria-hidden="true">
    <rect width="28" height="20" rx="1"/>
    <path d="M1 1l13 10L27 1" fill="none" stroke="#1a1818" stroke-width="2"/>
  </svg>
  <div class="contact contact--light" style="top:272px">hal@halsremedies.example</div>

  <svg class="icon" style="top:310px" width="28" height="28" viewBox="0 0 28 28" aria-hidden="true">
    <circle cx="14" cy="15" r="11" fill="none" stroke="#9ac43c" stroke-width="2.5"/>
    <path d="M14 9v6l4 3" fill="none" stroke="#9ac43c" stroke-width="2.5"/>
    <path d="M2 6l5-5M26 6l-5-5" stroke="#9ac43c" stroke-width="2.5"/>
  </svg>
  <div class="hours">
    Monday-Friday <b>8am-7 pm</b><br>
    Saturday <b>8am-12 pm</b><br>
    <b>Sunday Closed.</b>
  </div>

  <div class="website">www.halsremedies.example</div>
</section>

</body>
</html>
```